Offer banner redesign / Simplifying existing banner

We have a banner there customer can click on to get an offer. We want to simplify this banner and to get it to at minimum. We are not clear about how it shoulderstand look like, but the actual banner you can see here (It's at the top of the page): https://ofenrohr-lagerhaus.de/kaminsysteme/ We want to get rid of the icons and to reduce the size of the baner. The baner shoulderstand contain the Following text: Affordable chimney using installation service button text: Request free quote

Target Market(s)

Customers from age of 40yrs.

Requirements
Must have
• Clear and good visible button
Nice to have
• It Should be simple and striking.

```html
<!DOCTYPE html>
<html lang="de">
<head>
<meta charset="utf-8">
<title>Angebotsbanner – Schornstein</title>
<link rel="stylesheet" href="https://fonts.googleapis.com/css2?family=Arimo:wght@400;700&display=swap">
<style>
  :root {
    --banner-bg: #333333;
    --accent-orange: #f9b233;
    --button-frame: #5e5f62;
    --button-frame-edge: #9a9b9e;
    --button-text: #ffffff;
    --text-shadow: rgba(0, 0, 0, 0.8);
  }
  html, body {
    margin: 0;
    padding: 0;
    width: 1200px;
    height: 171px;
    overflow: hidden;
    background: var(--banner-bg);
  }
  .offer-banner {
    position: relative;
    width: 1200px;
    height: 171px;
    background: var(--banner-bg);
    font-family: "Arimo", Arial, Helvetica, sans-serif;
  }
  .offer-headline {
    position: absolute;
    left: 45px;
    top: 28px;
    margin: 0;
    font-weight: 400;
    font-size: 40px;
    line-height: 52px;
    letter-spacing: 0.6px;
    color: var(--accent-orange);
    text-shadow: 1px 2px 2px var(--text-shadow);
    white-space: nowrap;
  }
  .offer-button-frame {
    position: absolute;
    left: 681px;
    top: 37px;
    width: 467px;
    height: 98px;
    box-sizing: border-box;
    background: var(--button-frame);
    border: 1px solid var(--button-frame-edge);
    padding: 9px;
  }
  .offer-button {
    display: flex;
    align-items: center;
    justify-content: center;
    width: 100%;
    height: 100%;
    background: var(--accent-orange);
    color: var(--button-text);
    font-weight: 700;
    font-size: 24px;
    letter-spacing: 0.9px;
    text-decoration: none;
    white-space: nowrap;
    text-shadow: 1px 1px 2px rgba(0, 0, 0, 0.45);
  }
</style>
</head>
<body>
  <div class="offer-banner">
    <h2 class="offer-headline">Preiswerter Schornstein<br>wahlweise mit Montageservice</h2>
    <div class="offer-button-frame">
      <a class="offer-button" href="#angebot">Kostenloses Angebot Anfordern</a>
    </div>
  </div>
</body>
</html>
```